Construction Company Website Design

I need a Website Design for a Construction Company. I have attached logo and business card design files (a.i) to match styles and text for the website. I will need design for 3 pages:
1. A Home page
2. A secondary page (will be different information pages)
3. A contact page with submision form
Website to look professional and match the 'theme' across all pages, using main colours / reverse colours as per design files. Must be clear it is a construction related website without being over the top. Happy for the construction related details (whether that be images/outlines/backgrounds etc to be fairly subtle and not overbearing on the contect of the pages. It will be the content that will be most important, not the images within.

Content has not yet been fully completed but attached is a site map. Each page will need a space for the insertion of the relevant heading and associated content for that particular page. Example can be used as per attached map. If it is preferable to have content completed for this to be a more succesful project please advise and I will complete and submit.

Target Market(s)

Clients for potential construction projects. These could be a range of people. All would be very professional, well educated and put a substantial expection on the quality of website provided.

Industry/Entity Type

Construction

Number of Pages Required

3 page

Font styles to use
Serif
Sans Serif
Other font styles liked:
• fonts preferable as per design files provided unless designer beleives a different font would suit better

Requirements
Must have
• Colour scheme to match logo and business card files provided. Fonts that match as per provided files. Pages must be consistent with the theme carrying across all pages. All pages must have contact details at the bottom of the page.
• Contents of page 1 - 'Home page': multiple tab options / logo link
• Contents of page 2 - 'Secondary page': Top and side navigation / area for information and/or images.
• Contents of page - 'Contact us page': Top and side navigation / Submission form / area for logos such as linkdin, facebook etc.
Nice to have
• Would be good to have a or some generic construction related images - outlines / shadows / effects etc. These might be background images or outlines related to the relevant industry and are consistent across the pages. Could be outlines of buildings, images of men with hardhats etc etc. Good to see colour scheme as per design files used
Should not have
• No pictures of houses. Generally no photos. If any imagery of people must not show faces/details.

```html
<!DOCTYPE html>
<html lang="en">
<head>
<meta charset="utf-8">
<title>Halvern Builders</title>
<link href="https://fonts.googleapis.com/css2?family=Exo+2:wght@300;400;600&family=Lato:wght@400;700&display=swap" rel="stylesheet">
<style>
:root{
  --blue:#1aa3e8;
  --ink:#222;
  --text:#444;
  --paper:#f4f4f4;
  --white:#fff;
  --dark:#262626;
}
*{box-sizing:border-box;margin:0;padding:0}
html,body{width:1200px;height:3956px;overflow:hidden}
body{font-family:"Lato",sans-serif;color:var(--text);background:var(--white);position:relative}
.abs{position:absolute}
.h-sec{font-family:"Exo 2",sans-serif;font-size:34px;letter-spacing:3px;color:var(--ink);font-weight:600;white-space:nowrap}
.h-sec span{font-weight:300;color:var(--text);letter-spacing:2px}
.h-sec.center{width:1200px;text-align:center;left:0}
.rule{height:4px;width:80px;background:var(--blue)}
.btn{background:var(--blue);color:#fff;font-size:14px;font-weight:700;letter-spacing:1px;text-align:center;line-height:40px;height:40px}
.copy{font-size:14px;line-height:21px;color:var(--text)}
.arrow{width:24px;height:24px;border-radius:50%;display:flex;align-items:center;justify-content:center}
/* header */
.site-header{top:0;left:0;width:1200px;height:80px;background:#fff}
.wordmark{font-family:"Lato",sans-serif;font-size:22px;font-weight:700;letter-spacing:1px;color:#333;white-space:nowrap}
.site-header .wordmark{left:190px;top:26px}
.main-nav{left:554px;top:0;display:flex;height:80px}
.main-nav a{font-size:13px;color:#333;text-decoration:none;padding:0 20px;line-height:80px;letter-spacing:.5px}
.main-nav a.active{background:var(--blue);color:#fff}
/* hero */
.hero{top:80px;left:0;width:1200px;height:627px;background:linear-gradient(120deg,#e7b26c 0%,#a8795a 30%,#5a4a46 60%,#6b6a4f 80%,#c9d04a 100%)}
.hero-shade{inset:0;background:rgba(0,0,0,.25)}
.hero-title{top:228px;width:1200px;text-align:center;color:#fff;font-family:"Exo 2",sans-serif;line-height:60px}
.hero-title .l1{font-size:48px;font-weight:600;letter-spacing:4px}
.hero-title .l2{font-size:48px;font-weight:300;letter-spacing:2px}
/* services */
.services{top:1450px;left:0;width:1200px;height:602px;background:var(--paper)}
.svc{width:196px}
.svc .img{height:195px}
.svc h3{font-size:15px;font-weight:700;color:var(--ink);margin-top:22px;letter-spacing:.5px}
.svc .rule{width:60px;height:3px;margin:10px 0 14px}
.svc .more{margin-top:8px;width:16px;height:16px;border:1.5px solid var(--blue);border-radius:50%}
/* stats */
.stats{top:2052px;left:0;width:1200px;height:211px;background:linear-gradient(90deg,#2a2f34,#1b1f23 50%,#2c3136)}
.stat{width:160px;text-align:center;color:#fff;top:46px}
.stat b{display:block;font-size:17px;margin-top:10px}
.stat small{font-size:14px;color:#ddd}
/* projects */
.proj{width:196px;height:309px;top:2452px}
.proj .cap{position:absolute;left:14px;bottom:14px;color:#fff}
.proj .cap b{font-size:14px;display:block}
.proj .cap small{font-size:11px;color:#ddd}
/* news */
.news{top:2932px;left:0;width:1200px;height:696px;background:var(--paper)}
.card{background:#fff;width:260px;height:372px;top:180px;box-shadow:0 2px 8px rgba(0,0,0,.08)}
.card .img{height:174px}
.card .pin{position:absolute;left:110px;top:150px;width:40px;height:40px;border-radius:50%;background:var(--blue);border:3px solid #fff;display:flex;align-items:center;justify-content:center}
.card h4{position:absolute;left:24px;top:214px;font-size:17px;color:var(--ink);font-weight:700}
.card .rule{position:absolute;left:24px;top:242px;width:50px;height:3px}
.card .meta{position:absolute;left:24px;top:262px;font-size:11px;color:var(--text)}
.card .meta span{color:var(--blue)}
.card p{position:absolute;left:24px;top:292px;width:212px;font-size:12px;line-height:17px}
/* footer */
.site-footer{top:3628px;left:0;width:1200px;height:328px;background:var(--dark);color:#fff}
.site-footer .wordmark{left:190px;top:54px;color:#fff}
.f-contact{font-size:12px;line-height:16px;color:#ddd}
.f-contact li{list-style:none;display:flex;gap:12px;margin-bottom:10px}
.f-head{font-family:"Exo 2",sans-serif;font-size:22px;font-weight:600;letter-spacing:2px;white-space:nowrap}
.f-head span{font-weight:300}
.tags{display:grid;grid-template-columns:repeat(2,auto);gap:9px 12px;justify-content:start}
.tags a{border:1px solid #fff;color:#fff;font-size:11px;padding:2px 8px;text-decoration:none;width:max-content}
.tags a.on{background:var(--blue);border-color:var(--blue)}
.gallery{display:grid;grid-template-columns:110px 110px;gap:4px}
.gallery div{height:72px;background:linear-gradient(160deg,#7d9bb3,#3a4d5f)}
.social{display:flex;gap:20px}
.social i{width:16px;height:16px;background:#fff;display:block;border-radius:50%}
.f-line{left:190px;top:278px;width:820px;height:1px;background:#555}
.f-copy{top:294px;width:1200px;text-align:center;font-size:13px;font-weight:700}
</style>
</head>
<body>

<header class="site-header abs">
  <div class="wordmark abs">Halvern Builders</div>
  <nav class="main-nav abs">
    <a class="active" href="#">ABOUT</a>
    <a href="#">SERVICES ▾</a>
    <a href="#">PROJECTS</a>
    <a href="#">CULTURE</a>
    <a href="#">NEWS</a>
    <a href="#">CONTACT</a>
  </nav>
</header>

<section class="hero abs" role="img" aria-label="Construction worker in a high-visibility vest holding a yellow hard hat at sunset on a building site">
  <div class="hero-shade abs"></div>
  <h1 class="hero-title abs"><div class="l1">WELLCOME TO</div><div class="l2">Halvern Builders</div></h1>
  <div class="arrow abs" style="left:82px;top:308px;background:#222"><svg width="10" height="10" viewBox="0 0 10 10"><path d="M6.5 1.5 3 5l3.5 3.5" stroke="#fff" stroke-width="1.6" fill="none"/></svg></div>
  <div class="arrow abs" style="left:1096px;top:308px;background:var(--blue)"><svg width="10" height="10" viewBox="0 0 10 10"><path d="M3.5 1.5 7 5 3.5 8.5" stroke="#fff" stroke-width="1.6" fill="none"/></svg></div>
</section>

<section class="about">
  <h2 class="h-sec abs" style="left:190px;top:790px">ABOUT <span>Us</span></h2>
  <div class="rule abs" style="left:190px;top:846px"></div>
  <p class="copy abs" style="left:190px;top:884px;width:330px">Lorem Ipsum is simply dummy text of the printing and typesetting industry. Lorem Ipsum has been the industry's standard dummy text ever since the 1500s, when an unknown printer took a galley of type and scrambled it to make a type specimen book.</p>
  <div class="btn abs" style="left:190px;top:996px;width:140px">READ MORE</div>
  <div class="abs" role="img" aria-label="Video still of a building under construction" style="left:601px;top:773px;width:409px;height:274px;background:linear-gradient(160deg,#7a6e62,#3c3a38)">
    <svg class="abs" style="left:168px;top:100px" width="74" height="74" viewBox="0 0 74 74"><circle cx="37" cy="37" r="34" fill="#fff" stroke="#333" stroke-width="3"/><path d="M29 22v30l25-15z" fill="#1aa3e8"/></svg>
  </div>
  <div class="abs" role="img" aria-label="Glass office towers against a blue sky" style="left:190px;top:1094px;width:406px;height:275px;background:linear-gradient(170deg,#6f9fd0,#2d4a6c 70%,#1c2c40)"></div>
  <h2 class="h-sec abs" style="left:654px;top:1108px">OUR <span>Mission</span></h2>
  <div class="rule abs" style="left:654px;top:1162px"></div>
  <p class="copy abs" style="left:654px;top:1198px;width:350px">Lorem Ipsum is simply dummy text of the printing and typesetting industry. Lorem Ipsum has been the industry's standard dummy text ever since the 1500s, when an unknown printer took a galley of type and scrambled it to make a type specimen book.</p>
  <div class="btn abs" style="left:654px;top:1313px;width:140px">READ MORE</div>
</section>

<section class="services abs">
  <h2 class="h-sec center abs" style="top:56px">OUR <span>Services</span></h2>
  <div class="rule abs" style="left:560px;top:112px"></div>
  <div class="svc abs" style="left:190px;top:167px"><div class="img" role="img" aria-label="Tower cranes over a high-rise" style="background:linear-gradient(170deg,#9fc0de,#5a6c7c)"></div><h3>COMMERCIAL</h3><div class="rule"></div><p class="copy">Lorem Ipsum is simply dummy text of the printing and typesetting industry.</p><div class="more"></div></div>
  <div class="svc abs" style="left:396px;top:167px"><div class="img" role="img" aria-label="Timber house frame with green roof" style="background:linear-gradient(170deg,#7fb5e0,#7c8d4a 55%,#a07a4e)"></div><h3>RESIDENTIAL</h3><div class="rule"></div><p class="copy">Lorem Ipsum is simply dummy text of the printing and typesetting industry.</p><div class="more"></div></div>
  <div class="svc abs" style="left:604px;top:167px"><div class="img" role="img" aria-label="Foundation works with reinforcement on site" style="background:linear-gradient(170deg,#b08a64,#5c4330)"></div><h3>MAINTENANCE</h3><div class="rule"></div><p class="copy">Lorem Ipsum is simply dummy text of the printing and typesetting industry.</p><div class="more"></div></div>
  <div class="svc abs" style="left:812px;top:167px"><div class="img" role="img" aria-label="Workers in hard hats reviewing plans indoors" style="background:linear-gradient(170deg,#9a9a94,#4e4a44)"></div><h3>MANAGEMENT</h3><div class="rule"></div><p class="copy">Lorem Ipsum is simply dummy text of the printing and typesetting industry.</p><div class="more"></div></div>
</section>

<section class="stats abs" role="img" aria-label="Scaffolding silhouette background">
  <div class="stat abs" style="left:200px"><svg width="44" height="44" viewBox="0 0 44 44"><path d="M6 20h7v20H6zM16 40V20l8-14c3 0 4 2 3 6l-2 6h11c2 0 3 2 2 4l-4 15c-1 2-2 3-4 3z" fill="none" stroke="#1aa3e8" stroke-width="3" stroke-linejoin="round"/></svg><b>100%</b><small>Service Quality</small></div>
  <div class="stat abs" style="left:410px"><svg width="44" height="44" viewBox="0 0 44 44"><circle cx="22" cy="22" r="18" fill="none" stroke="#1aa3e8" stroke-width="3"/><circle cx="16" cy="18" r="2" fill="#1aa3e8"/><circle cx="28" cy="18" r="2" fill="#1aa3e8"/><path d="M14 25q8 8 16 0" fill="none" stroke="#1aa3e8" stroke-width="3"/></svg><b>3895</b><small>Satisfied Clients</small></div>
  <div class="stat abs" style="left:621px"><svg width="44" height="44" viewBox="0 0 44 44"><circle cx="22" cy="22" r="18" fill="none" stroke="#1aa3e8" stroke-width="3"/><path d="M13 22l7 7 12-14" fill="none" stroke="#1aa3e8" stroke-width="3.5"/></svg><b>580</b><small>Completed Projects</small></div>
  <div class="stat abs" style="left:832px"><svg width="44" height="44" viewBox="0 0 44 44"><path d="M22 3l5.6 12.6 13.4 1.2-10.2 9 3.1 13.2L22 32l-11.9 7 3.1-13.2-10.2-9 13.4-1.2z" fill="#1aa3e8"/></svg><b>20</b><small>Year Of Experience</small></div>
</section>

<section class="projects">
  <h2 class="h-sec center abs" style="top:2336px">RECENTLY <span>Projects</span></h2>
  <div class="rule abs" style="left:560px;top:2392px"></div>
  <div class="arrow abs" style="left:82px;top:2596px;background:#222"><svg width="10" height="10" viewBox="0 0 10 10"><path d="M6.5 1.5 3 5l3.5 3.5" stroke="#fff" stroke-width="1.6" fill="none"/></svg></div>
  <div class="proj abs" role="img" aria-label="Modern dark apartment facade" style="left:190px;background:linear-gradient(170deg,#5a6470,#2a2f36)"><div class="cap"><b>Project Name</b><small>Country,City</small></div></div>
  <div class="proj abs" role="img" aria-label="Apartment block with balconies" style="left:396px;background:linear-gradient(170deg,#55595e,#24272b)"><div class="cap" style="top:14px;bottom:auto"><b>Project Name</b><small>Country,City</small></div>
    <svg class="abs" style="left:80px;top:136px" width="36" height="36" viewBox="0 0 36 36" fill="none" stroke="#fff" stroke-width="3"><path d="M2 12V2h10M24 2h10v10M34 24v10H24M12 34H2V24"/></svg></div>
  <div class="proj abs" role="img" aria-label="Glass tower with white fins" style="left:604px;background:linear-gradient(170deg,#8fb4d8,#3c5674)"><div class="cap"><b>Project Name</b><small>Country,City</small></div></div>
  <div class="proj abs" role="img" aria-label="Building interior with glass railings" style="left:812px;background:linear-gradient(170deg,#c2c6c4,#6b5a4a)"><div class="cap"><b>Project Name</b><small>Country,City</small></div></div>
  <div class="arrow abs" style="left:1096px;top:2596px;background:var(--blue)"><svg width="10" height="10" viewBox="0 0 10 10"><path d="M3.5 1.5 7 5 3.5 8.5" stroke="#fff" stroke-width="1.6" fill="none"/></svg></div>
  <div class="btn abs" style="left:530px;top:2830px;width:140px">VIEW ALL</div>
</section>

<section class="news abs">
  <h2 class="h-sec center abs" style="top:72px">LATSET <span>News</span></h2>
  <div class="rule abs" style="left:560px;top:128px"></div>
  <div class="arrow abs" style="left:82px;top:344px;background:#222"><svg width="10" height="10" viewBox="0 0 10 10"><path d="M6.5 1.5 3 5l3.5 3.5" stroke="#fff" stroke-width="1.6" fill="none"/></svg></div>
  <article class="card abs" style="left:190px"><div class="img" role="img" aria-label="Two-storey building under a blue sky" style="background:linear-gradient(180deg,#6aa4dc,#9aa3a0 60%,#5c7a45)"></div><div class="pin"><svg width="16" height="16" viewBox="0 0 16 16" fill="none" stroke="#fff" stroke-width="2"><path d="M7 9l2-2M6 6l-3 3a2.2 2.2 0 003 3l3-3M10 10l3-3a2.2 2.2 0 00-3-3L7 7"/></svg></div><h4>NEWS 1</h4><div class="rule"></div><div class="meta">April 19 2018 &nbsp; <span>■</span> 12 Comments</div><p>Lorem Ipsum is simply dummy text of the printing and typesetting industry.</p></article>
  <article class="card abs" style="left:467px"><div class="img" role="img" aria-label="Curved white residential tower" style="background:linear-gradient(180deg,#b8c6d2,#6f7884)"></div><div class="pin"><svg width="16" height="16" viewBox="0 0 16 16" fill="none" stroke="#fff" stroke-width="2"><path d="M7 9l2-2M6 6l-3 3a2.2 2.2 0 003 3l3-3M10 10l3-3a2.2 2.2 0 00-3-3L7 7"/></svg></div><h4>NEWS 2</h4><div class="rule"></div><div class="meta">April 19 2018 &nbsp; <span>■</span> 12 Comments</div><p>Lorem Ipsum is simply dummy text of the printing and typesetting industry.</p></article>
  <article class="card abs" style="left:746px"><div class="img" role="img" aria-label="Cream building corner against blue sky" style="background:linear-gradient(180deg,#4f8fd0,#cdb28a 70%)"></div><div class="pin"><svg width="16" height="16" viewBox="0 0 16 16" fill="none" stroke="#fff" stroke-width="2"><path d="M7 9l2-2M6 6l-3 3a2.2 2.2 0 003 3l3-3M10 10l3-3a2.2 2.2 0 00-3-3L7 7"/></svg></div><h4>NEWS 3</h4><div class="rule"></div><div class="meta">April 19 2018 &nbsp; <span>■</span> 12 Comments</div><p>Lorem Ipsum is simply dummy text of the printing and typesetting industry.</p></article>
  <div class="arrow abs" style="left:1096px;top:344px;background:var(--blue)"><svg width="10" height="10" viewBox="0 0 10 10"><path d="M3.5 1.5 7 5 3.5 8.5" stroke="#fff" stroke-width="1.6" fill="none"/></svg></div>
  <div class="btn abs" style="left:530px;top:604px;width:140px">VIEW ALL</div>
</section>

<footer class="site-footer abs">
  <div class="wordmark abs">Halvern Builders</div>
  <ul class="f-contact abs" style="left:190px;top:120px">
    <li><svg width="12" height="12" viewBox="0 0 12 12"><path d="M2 1l2.5 2-1 1.5a7 7 0 004 4l1.5-1 2 2.5-1.5 1.5C5 11 1 7 .5 2.5z" fill="#fff"/></svg>0400 123 987</li>
    <li><svg width="12" height="12" viewBox="0 0 12 12"><rect x="1" y="2.5" width="10" height="7" fill="none" stroke="#fff"/><path d="M1 3l5 4 5-4" fill="none" stroke="#fff"/></svg>hello@halvernbuild.example</li>
    <li><svg width="12" height="12" viewBox="0 0 12 12"><circle cx="6" cy="6" r="5" fill="none" stroke="#fff"/><path d="M1 6h10M6 1v10" stroke="#fff"/></svg>www.halvernbuild.example</li>
    <li><svg width="12" height="12" viewBox="0 0 12 12"><path d="M6 11S2 7 2 4.5a4 4 0 018 0C10 7 6 11 6 11z" fill="#fff"/></svg><span>14 Ridge Lane<br>Westbrook 2190</span></li>
  </ul>
  <div class="social abs" style="left:190px;top:236px"><i></i><i></i><i></i><i></i><i></i></div>
  <h3 class="f-head abs" style="left:570px;top:40px">ITEM <span>Tags</span></h3>
  <div class="rule abs" style="left:570px;top:72px;width:120px;height:3px"></div>
  <div class="tags abs" style="left:570px;top:88px">
    <a class="on" href="#">About</a><a href="#">Services</a>
    <a href="#">Projects</a><a href="#">Culture</a>
    <a href="#">Latest News</a><a href="#">Legal</a>
    <a href="#">Privacy policy</a><span></span>
    <a href="#">Terms &amp; Condition</a><span></span>
    <a href="#">Certification</a>
  </div>
  <h3 class="f-head abs" style="left:780px;top:40px">GALLERY <span>Slider</span></h3>
  <div class="rule abs" style="left:780px;top:72px;width:224px;height:3px"></div>
  <div class="gallery abs" role="img" aria-label="Grid of recent building photos" style="left:780px;top:86px"><div></div><div></div><div></div><div></div></div>
  <div class="f-line abs"></div>
  <p class="f-copy abs">Copyright © halvernbuild 2018. All Right Reserved.</p>
</footer>

</body>
</html>
```